One Page Website for Personal Trainer in London

I have a logo and need a one page website designed around my branding. I am a freelance Personal Trainer based in London specialising in bodyweight training for men and women. I would like the site to be modern and clean but not overtly urban in design.
I need the following headings:
About Me
My Services
Events
Blog
I don't need them to be seperate pages but if they can link to further down the page that would be great.
Industry/Entity Type
Personal Trainer
Coding
Coded - Design and coding required
Number of Pages Required
1 page
Requirements
Must have
- I need the following headings:
- About Me
- My Services
- Events
- Blog
- mobile friendly formatting
- health and fitness related photography
- Colour scheme in keeping with my existing logo

```html
<!DOCTYPE html>
<html lang="en">
<head>
<meta charset="utf-8">
<title>Maren Holt – Personal Trainer</title>
<link rel="stylesheet" href="https://fonts.googleapis.com/css2?family=Oswald:wght@400;500;600&family=Open+Sans:wght@400;600;700&display=swap">
<style>
:root{
  --orange:#f7941d;
  --orange-dark:#e07f0a;
  --ink:#222222;
  --text:#555555;
  --muted:#8a8a8a;
  --dark:#1c1c1c;
  --dark-2:#2a2a2a;
  --light:#f3f3f3;
  --white:#ffffff;
  --line:#dddddd;
}
*{margin:0;padding:0;box-sizing:border-box}
html,body{width:1200px;height:3672px;overflow:hidden}
body{font-family:"Open Sans",Arial,sans-serif;color:var(--text);background:var(--white);font-size:13px;line-height:1.7}
h1,h2,h3,h4,.nav a,.brand-name{font-family:"Oswald","Arial Narrow",sans-serif}
.section-title{font-size:34px;font-weight:500;color:var(--ink);text-align:center;letter-spacing:1px;text-transform:uppercase}
.section-title::after{content:"";display:block;width:50px;height:3px;background:var(--orange);margin:12px auto 0}
.on-dark .section-title{color:var(--white)}

/* hero */
.hero{position:relative;height:700px;background:linear-gradient(120deg,#5a4a45 0%,#3b3a3f 40%,#6b5a52 70%,#2f2e33 100%)}
.hero-photo{position:absolute;inset:0;background:radial-gradient(ellipse at 30% 40%,rgba(210,120,130,.45),transparent 55%),radial-gradient(ellipse at 75% 60%,rgba(80,110,160,.35),transparent 50%),linear-gradient(180deg,rgba(0,0,0,.35),rgba(0,0,0,.15) 40%,rgba(0,0,0,.45))}
.topbar{position:absolute;top:0;left:0;right:0;height:160px;padding:24px 90px 0}
.brand{position:absolute;left:90px;top:24px;display:flex;align-items:center;gap:12px}
.brand-dot{width:54px;height:54px;border-radius:50%;background:var(--orange)}
.brand-name{color:var(--white);font-size:26px;font-weight:500;letter-spacing:1px;line-height:1}
.brand-sub{display:block;font-size:11px;letter-spacing:3px;margin-top:4px}
.contact-strip{position:absolute;right:90px;top:38px;display:flex;gap:40px;color:var(--white);font-size:12px;line-height:1.4}
.contact-strip .item{display:flex;align-items:center;gap:10px}
.contact-strip .ico{width:34px;height:34px;border-radius:50%;background:var(--orange);display:flex;align-items:center;justify-content:center}
.nav{position:absolute;right:90px;top:118px;display:flex;gap:30px}
.nav a{color:var(--white);text-decoration:none;font-size:14px;letter-spacing:1px;padding-bottom:8px;border-bottom:2px solid transparent}
.nav a.active{border-color:var(--orange)}
.hero-mark{position:absolute;left:50%;top:330px;transform:translateX(-50%);display:flex;align-items:center;gap:20px;color:var(--white)}
.hero-mark .brand-dot{width:110px;height:110px}
.hero-mark h1{font-size:64px;font-weight:600;line-height:1;letter-spacing:2px}
.hero-mark p{font-family:"Oswald","Arial Narrow",sans-serif;font-size:40px;line-height:1.1;letter-spacing:2px}

/* about */
.about{display:flex;height:540px}
.about-photo{width:600px;height:540px;background:linear-gradient(180deg,#8fb4c9 0%,#c9d6d8 40%,#d8c6a8 70%,#bfa98a 100%)}
.about-body{flex:1;padding:110px 90px 0 60px}
.about-body h2{font-size:34px;font-weight:500;color:var(--ink);letter-spacing:1px}
.about-body h2::after{content:"";display:block;width:50px;height:3px;background:var(--orange);margin-top:10px}
.about-body p{margin-top:22px;font-size:13px}

/* services */
.services{height:720px;background:linear-gradient(180deg,rgba(20,20,20,.88),rgba(20,20,20,.88)),linear-gradient(90deg,#4a4a4a,#2c2c2c,#555)}
.services .section-title{padding-top:90px}
.service-grid{display:flex;justify-content:space-between;padding:70px 90px 0}
.service{width:230px;text-align:center;color:#c8c8c8}
.service-icon{width:110px;height:110px;border-radius:50%;background:var(--orange);margin:0 auto;display:flex;align-items:center;justify-content:center;border:6px solid var(--white)}
.service h3{color:var(--white);font-size:17px;font-weight:500;margin-top:26px;letter-spacing:1px;text-transform:uppercase}
.service p{margin-top:10px;font-size:12px}

/* events */
.events{height:760px;padding-top:80px}
.event-grid{display:flex;justify-content:space-between;padding:70px 100px 0}
.event{width:300px;text-align:center;border-bottom:1px solid var(--line);padding-bottom:26px}
.event-photo{position:relative;height:200px}
.event-photo.a{background:linear-gradient(135deg,#b76a2a,#3a2c25 60%,#1e1e1e)}
.event-photo.b{background:linear-gradient(135deg,#7fa85a,#c9b48a 55%,#4e6b3a)}
.event-photo.c{background:linear-gradient(135deg,#6b3a3a,#b24a3a 50%,#2a2a2a)}
.date-badge{position:absolute;left:50%;bottom:-28px;transform:translateX(-50%);width:58px;height:58px;border-radius:50%;background:var(--orange);border:3px solid var(--white);color:var(--white);font-family:"Oswald",sans-serif;font-size:11px;line-height:1.15;display:flex;flex-direction:column;align-items:center;justify-content:center}
.date-badge b{font-size:18px;font-weight:500}
.event h3{font-size:17px;font-weight:400;color:var(--ink);margin-top:48px}
.event p{margin-top:12px;font-size:12px}

/* blog */
.blog{height:600px;background:linear-gradient(180deg,rgba(25,25,25,.9),rgba(25,25,25,.9)),linear-gradient(90deg,#5a5a5a,#333)}
.blog .section-title{padding-top:70px}
.post-grid{display:flex;justify-content:space-between;padding:40px 100px 0}
.post{width:300px;color:#bdbdbd}
.post-photo{height:180px}
.post-photo.a{background:linear-gradient(135deg,#9ba4ad,#4a4f58 60%,#2a2d33)}
.post-photo.b{background:linear-gradient(135deg,#5a3b2e,#a6623f 55%,#2e2624)}
.post-photo.c{background:linear-gradient(135deg,#c9b8a0,#8a6f56 50%,#3a302a)}
.post h3{color:var(--white);font-size:17px;font-weight:400;margin-top:16px}
.post time{display:block;color:var(--orange);font-size:12px;margin-top:2px}
.post p{margin-top:6px;font-size:12px}

/* footer */
.site-footer{height:300px;background:var(--light);display:flex;padding:50px 90px 0;gap:60px}
.footer-brand{width:230px;text-align:center}
.footer-brand .brand-line{display:flex;align-items:center;justify-content:center;gap:10px}
.footer-brand .brand-dot{width:46px;height:46px}
.footer-brand .brand-name{color:var(--ink);font-size:24px}
.socials{display:flex;justify-content:center;gap:8px;margin-top:22px}
.socials span{width:26px;height:26px;border-radius:50%;border:2px solid var(--ink)}
.footer-col h4{font-size:15px;font-weight:500;color:var(--ink);letter-spacing:1px;text-transform:uppercase}
.footer-col h4::after{content:"";display:block;width:30px;height:2px;background:var(--orange);margin-top:8px}
.footer-col ul{list-style:none;margin-top:14px;font-size:12px}
.footer-col li{display:flex;align-items:center;gap:10px;margin-bottom:8px}
.footer-col li i{width:10px;height:10px;border-radius:50%;background:var(--orange);flex:none}
.contact-col{width:200px}
.news-col{width:260px}
.news-col p{margin-top:14px;font-size:12px}
.news-input{margin-top:14px;height:36px;border:1px solid var(--line);background:var(--white);font-size:12px;color:var(--muted);padding:8px 12px}
.news-btn{margin-top:10px;display:inline-block;background:var(--orange);color:var(--white);font-weight:700;font-size:12px;padding:8px 22px;letter-spacing:1px}
.links-col li::before{content:"›";color:var(--orange);margin-right:2px}
.copyright{height:52px;background:var(--dark);color:#9a9a9a;font-size:11px;text-align:center;line-height:52px}
</style>
</head>
<body>

<header class="hero">
  <div class="hero-photo" role="img" aria-label="Group bodyweight class doing plank push-ups in a gym"></div>
  <div class="topbar">
    <div class="brand">
      <span class="brand-dot"></span>
      <span class="brand-name">MAREN HOLT<span class="brand-sub">PERSONAL TRAINING</span></span>
    </div>
    <div class="contact-strip">
      <div class="item"><span class="ico"><svg width="16" height="16" viewBox="0 0 24 24" fill="#fff"><path d="M6.6 10.8a15.1 15.1 0 0 0 6.6 6.6l2.2-2.2a1 1 0 0 1 1-.25 11.4 11.4 0 0 0 3.6.57 1 1 0 0 1 1 1V20a1 1 0 0 1-1 1A17 17 0 0 1 3 4a1 1 0 0 1 1-1h3.5a1 1 0 0 1 1 1c0 1.25.2 2.45.57 3.57a1 1 0 0 1-.25 1z"/></svg></span><span>Call Us<br>+44 20 7946 0321</span></div>
      <div class="item"><span class="ico"><svg width="16" height="16" viewBox="0 0 24 24" fill="#fff"><path d="M3 5h18v14H3z" fill="none" stroke="#fff" stroke-width="2"/><path d="M3 5l9 7 9-7" fill="none" stroke="#fff" stroke-width="2"/></svg></span><span>E - Mail<br>info@marenholt.com</span></div>
    </div>
    <nav class="nav">
      <a href="#about" class="active">ABOUT ME</a>
      <a href="#services">MY SERVICES</a>
      <a href="#events">EVENTS</a>
      <a href="#blog">BLOG</a>
      <a href="#contact">CONTACT</a>
    </nav>
  </div>
  <div class="hero-mark">
    <span class="brand-dot"></span>
    <div><h1>MAREN HOLT</h1><p>Personal Trainer</p></div>
  </div>
</header>

<section class="about" id="about">
  <div class="about-photo" role="img" aria-label="Trainer standing on a sunny beach"></div>
  <div class="about-body">
    <h2>ABOUT ME</h2>
    <p>Ut enim ad minima veniam, quis nostrum exercitationem ullam corporis suscipit laboriosam, nisi ut aliquid ex ea commodi consequatur. Quis autem vel eum iure reprehenderit qui in ea voluptate velit esse quam nihil molestiae consequatur, vel illum qui dolorem eum fugiat.</p>
    <p>Nemo enim ipsam voluptatem quia voluptas sit aspernatur aut odit aut fugit, sed quia consequuntur magni dolores eos qui ratione voluptatem sequi nesciunt. Neque porro quisquam est, qui dolorem ipsum quia dolor sit amet.</p>
  </div>
</section>

<section class="services on-dark" id="services">
  <h2 class="section-title">My Services</h2>
  <div class="service-grid">
    <div class="service">
      <div class="service-icon"><svg width="48" height="48" viewBox="0 0 48 48" fill="#fff"><rect x="6" y="16" width="6" height="16" rx="1"/><rect x="36" y="16" width="6" height="16" rx="1"/><rect x="12" y="21" width="24" height="6"/></svg></div>
      <h3>Personal Training</h3>
      <p>Sed ut perspiciatis unde omnis iste natus error sit voluptatem accusantium doloremque laudantium, totam rem aperiam eaque ipsa quae ab illo inventore.</p>
    </div>
    <div class="service">
      <div class="service-icon"><svg width="48" height="48" viewBox="0 0 48 48" fill="none" stroke="#fff" stroke-width="4" stroke-linecap="round"><circle cx="28" cy="9" r="4" fill="#fff" stroke="none"/><path d="M14 20l10-4 6 8 8 2M24 16l-4 12 8 6v8M20 28l-8 10"/></svg></div>
      <h3>Sports Coaching</h3>
      <p>Sed ut perspiciatis unde omnis iste natus error sit voluptatem accusantium doloremque laudantium, totam rem aperiam eaque ipsa quae ab illo inventore.</p>
    </div>
    <div class="service">
      <div class="service-icon"><svg width="48" height="48" viewBox="0 0 48 48" fill="none" stroke="#fff" stroke-width="3.5" stroke-linejoin="round"><path d="M24 40S6 29 6 17a9 9 0 0 1 18-3 9 9 0 0 1 18 3c0 12-18 23-18 23z"/><path d="M10 24h8l3-6 5 12 3-6h9"/></svg></div>
      <h3>Injury Management</h3>
      <p>Sed ut perspiciatis unde omnis iste natus error sit voluptatem accusantium doloremque laudantium, totam rem aperiam eaque ipsa quae ab illo inventore.</p>
    </div>
    <div class="service">
      <div class="service-icon"><svg width="48" height="48" viewBox="0 0 48 48" fill="none" stroke="#fff" stroke-width="4" stroke-linecap="round"><path d="M10 34l10-10 6 6 12-14"/><path d="M30 16h8v8"/></svg></div>
      <h3>Health &amp; Fitness</h3>
      <p>Sed ut perspiciatis unde omnis iste natus error sit voluptatem accusantium doloremque laudantium, totam rem aperiam eaque ipsa quae ab illo inventore.</p>
    </div>
  </div>
</section>

<section class="events" id="events">
  <h2 class="section-title">Events</h2>
  <div class="event-grid">
    <article class="event">
      <div class="event-photo a" role="img" aria-label="Kettlebell workout session"><span class="date-badge"><b>22</b>AUG</span></div>
      <h3>Nemo enim ipsam voluptatem</h3>
      <p>Sed ut perspiciatis unde omnis iste natus error sit voluptatem accusantium doloremque laudantium, totam rem aperiam, eaque ipsa quae ab illo inventore veritatis.</p>
    </article>
    <article class="event">
      <div class="event-photo b" role="img" aria-label="Outdoor group plank class"><span class="date-badge"><b>22</b>AUG</span></div>
      <h3>Nemo enim ipsam voluptatem</h3>
      <p>Sed ut perspiciatis unde omnis iste natus error sit voluptatem accusantium doloremque laudantium, totam rem aperiam, eaque ipsa quae ab illo inventore veritatis.</p>
    </article>
    <article class="event">
      <div class="event-photo c" role="img" aria-label="Indoor circuit training class"><span class="date-badge"><b>22</b>AUG</span></div>
      <h3>Nemo enim ipsam voluptatem</h3>
      <p>Sed ut perspiciatis unde omnis iste natus error sit voluptatem accusantium doloremque laudantium, totam rem aperiam, eaque ipsa quae ab illo inventore veritatis.</p>
    </article>
  </div>
</section>

<section class="blog on-dark" id="blog">
  <h2 class="section-title">From the Blog</h2>
  <div class="post-grid">
    <article class="post">
      <div class="post-photo a" role="img" aria-label="Athlete training on a gym machine"></div>
      <h3>Nemo enim ipsam voluptatem quia</h3>
      <time>August 22, 2017</time>
      <p>Sed ut perspiciatis unde omnis iste natus error sit voluptatem accusantium doloremque laudantium, totam rem aperiam.</p>
    </article>
    <article class="post">
      <div class="post-photo b" role="img" aria-label="Athlete doing battle rope training"></div>
      <h3>Nemo enim ipsam voluptatem quia</h3>
      <time>August 22, 2017</time>
      <p>Sed ut perspiciatis unde omnis iste natus error sit voluptatem accusantium doloremque laudantium, totam rem aperiam.</p>
    </article>
    <article class="post">
      <div class="post-photo c" role="img" aria-label="Trainer coaching a client with weights"></div>
      <h3>Nemo enim ipsam voluptatem quia</h3>
      <time>August 22, 2017</time>
      <p>Sed ut perspiciatis unde omnis iste natus error sit voluptatem accusantium doloremque laudantium, totam rem aperiam.</p>
    </article>
  </div>
</section>

<footer class="site-footer" id="contact">
  <div class="footer-brand">
    <div class="brand-line"><span class="brand-dot"></span><span class="brand-name">MAREN HOLT</span></div>
    <div class="socials"><span></span><span></span><span></span><span></span><span></span></div>
  </div>
  <div class="footer-col contact-col">
    <h4>Contact Us</h4>
    <ul>
      <li><i></i>12 Harrow Lane, London</li>
      <li><i></i>+44 20 7946 0321</li>
      <li><i></i>info@marenholt.com</li>
    </ul>
  </div>
  <div class="footer-col news-col">
    <h4>Sign Up for Newsletter</h4>
    <p>Subscribe to our newsletter for updates, tips and class news.</p>
    <div class="news-input">Email</div>
    <span class="news-btn">SIGN UP</span>
  </div>
  <div class="footer-col links-col">
    <h4>Quick Links</h4>
    <ul>
      <li>Home</li><li>About Me</li><li>My Services</li><li>Events</li><li>Blog</li><li>Contact</li>
    </ul>
  </div>
</footer>
<div class="copyright">© 2017 Maren Holt. All rights reserved.</div>

</body>
</html>
```